Venture Capital firm needs modern business cards

We are a Venture Capital firm within financial services/Asset management. The industry generally has basic business cards with black, blue and maybe green/yellow design elements.
Our firm has a four-colour swoosh logo. We are based in London and want to stand out, just a little bit!, from the crowd. Our company is called ROLK Investments and the 'C' stands for collaboration thus using artfolkhub is a natural portal for our business card design competition. Our logo came via artfolkhub too!
We use 'Venture Partner in Asset Management' as our tagline and this is Trademark registered. We operate in a conservative industry and we should not overstep our mark. The logo is colorful as it is and therefore the rest of the design should not be too fanciful.
The objective is twofold: make our logo element stick and memorable with our audience, whilst representing a conservative yet young image.
The Business Card obviously needs a field for Name, Surname, Job Title, Adress fields: Street, City, Postcode, Country, telefone and cell number, website address, etc.
We have uploaded the ai file. We trust that these are OK. If not, please advise.
Reason: We have have been busy with a client engagement. We will set the project as Guaranteed in return for the troubles we cause. Apologies for the confusion.
Thank you all for these great and creative design suggestions. The team is very happy with a number of your ideas! We will be in touch tomorrow to give individual feedback before the project closes on Friday. We look forward to working with some of you to narrow down your creations. Thank you, ROLK Investments team.
All,
Target Market(s)
Financial Services Professionals, Investors, Media, 35-70 years, mainly male, well educated
Industry/Entity Type
Conservative
Requirements
Must have
- We must make use of our logo and potential tagline 'Venture Partner in Asset Management' as we are establishing a new Brand and new company in the market.
We can use 'ROLK', 'ROLK Investments', and 'ROLK Investments'+tagline 'Venture Partner in Asset Management' or simply the four-colour swoosh plus the name of the company as part of the text. (see files)
All design elements are available in black or grey-scale if required. (grey scale swoosh attached).
Due to regulation we must have the following wording on the card in small print 'ROLK Investments is an Appointed Representative of Brambury Monetary Ventures Limited, which is authorised by the Pemberton Oversight Board'.
Nice to have
- We would consider designs that make use of different printing techniques such embossing/debossing, UV spot etc.
We attach our colour palette in the files section for your reference.
Should not have
- The font we use for our company name is 'EXO' so do not use a font style that clashes with the corporate fonts, please.
Do not use other design elements than the ones we provide in the file library as part of this project.

```html
<!DOCTYPE html>
<html lang="en">
<head>
<meta charset="utf-8">
<title>ROLK Investments – Business Cards</title>
<link href="https://fonts.googleapis.com/css2?family=Exo+2:wght@300;400;500&display=swap" rel="stylesheet">
<style>
  :root {
    --backdrop: #3a3a3a;
    --card: #232323;
    --card-edge: #1a1a1a;
    --ink: #e6e6e6;
    --ink-soft: #b9b9b9;
    --accent: #f0c419;
    --mark: #d9d9d9;
  }
  * { margin: 0; padding: 0; box-sizing: border-box; }
  html, body {
    width: 1200px; height: 715px; overflow: hidden;
    background: var(--backdrop);
    font-family: "Exo 2", sans-serif;
  }
  .canvas {
    position: relative; width: 1200px; height: 715px;
    display: flex; align-items: center; justify-content: center; gap: 50px;
  }
  .card {
    position: relative;
    width: 520px; height: 318px;
    background: var(--card);
    border: 1px solid var(--card-edge);
    border-radius: 3px;
    color: var(--ink);
  }
  .brand {
    position: absolute; left: 44px; top: 112px;
  }
  .brand-row { display: flex; align-items: center; gap: 12px; }
  .brand-dot {
    width: 34px; height: 34px; border-radius: 50%;
    background: var(--mark);
  }
  .brand-name {
    font-size: 62px; font-weight: 400; line-height: 1;
    color: var(--mark); letter-spacing: 1px;
  }
  .tagline {
    margin-top: 4px; margin-left: 46px;
    font-size: 8px; font-weight: 300; color: var(--ink-soft);
  }
  .regulatory {
    position: absolute; right: 40px; top: 112px; width: 140px;
    font-size: 10px; line-height: 1.35; font-weight: 300; color: var(--ink-soft);
  }
  .person { position: absolute; right: 40px; top: 56px; text-align: right; }
  .person-name { font-size: 22px; font-weight: 400; color: var(--accent); }
  .person-role { font-size: 13px; font-weight: 300; color: var(--ink); margin-top: -2px; }
  .contact {
    position: absolute; left: 300px; top: 128px;
    font-size: 14px; font-weight: 300; line-height: 1.4; list-style: none;
  }
  .contact-label { display: inline-block; width: 16px; color: var(--accent); }
  .address {
    position: absolute; left: 300px; top: 214px;
    font-size: 14px; font-weight: 300; line-height: 1.4; font-style: normal;
  }
</style>
</head>
<body>
<main class="canvas">
  <section class="card card-back">
    <div class="brand">
      <div class="brand-row"><span class="brand-dot"></span><span class="brand-name">rolk</span></div>
      <p class="tagline">Venture Partner in Asset Management</p>
    </div>
    <p class="regulatory">ROLK Investments is an Appointed Representative of Brambury Monetary Ventures Limited, which is authorised by the Pemberton Oversight Board</p>
  </section>

  <section class="card card-front">
    <div class="brand">
      <div class="brand-row"><span class="brand-dot"></span><span class="brand-name">rolk</span></div>
      <p class="tagline">Venture Partner in Asset Management</p>
    </div>
    <div class="person">
      <p class="person-name">Marcus Delborne</p>
      <p class="person-role">managing director</p>
    </div>
    <ul class="contact">
      <li><span class="contact-label">p</span>020 7946 0321</li>
      <li><span class="contact-label">c</span>07700 900 482</li>
      <li><span class="contact-label">e</span>info@rolkinvestment.com</li>
    </ul>
    <address class="address">
      48 Harrowgate Lane<br>
      London, EC2M 7QT<br>
      www.rolkinvestment.com
    </address>
  </section>
</main>
</body>
</html>
```